International Career Development Workshop

I need a Powerpoint revised and designed in a more professional manner for a presentation I will be giving. We are an International Education Company that provides students with Internships Abroad, and are expanding our career development programming to offer more guidance through on-site workshops. I am happy to send along our website to showcase the colors and fonts we use, but we tend to use royal blue, lime green, and white in our color scheme. The final design should communicate opportunity and self-awareness within college students.

Target Market(s)

College Students, University Partners, and International Education Community

Industry/Entity Type

Education

Font styles to use
Sans Serif

Colors
9bcb3b
0355a3
ffffff

Requirements
Must have
• Our logo, our color scheme, a unified, professional theme throughout, Watermark of our logo, thematic sections spread across four sections.
Nice to have
• Videos and graphics
Should not have
• Spelling Errors, sloppy design

```html
<!DOCTYPE html>
<html lang="en">
<head>
<meta charset="utf-8">
<title>International Career Development Workshop – Slide Set</title>
<link href="https://fonts.googleapis.com/css2?family=Roboto+Slab:wght@300;400;700&family=Lato:wght@300;400;700&display=swap" rel="stylesheet">
<style>
:root{
  --green:#9bcb3b;
  --green-dark:#86b52c;
  --blue:#0355a3;
  --ink:#3b3b3b;
  --grey:#6d6d6d;
  --grey-light:#9a9a9a;
  --canvas:#e6e6e6;
  --dark-band:#3f3f3f;
  --white:#ffffff;
}
*{margin:0;padding:0;box-sizing:border-box}
html,body{width:1200px;height:1142px;overflow:hidden;background:var(--canvas)}
body{position:relative;font-family:"Lato",sans-serif;color:var(--grey)}
.slide{position:absolute;width:380px;height:214px;background:var(--white);overflow:hidden}
.abs{position:absolute}
.corner{position:absolute;top:8px;right:13px;width:0;height:0;border-left:7px solid transparent;border-top:7px solid var(--blue)}
.corner span{position:absolute;top:-10px;left:1px;font-size:4.5px;color:var(--grey-light)}
.heading{position:absolute;font-family:"Roboto Slab",serif;text-transform:uppercase;line-height:1.15;font-size:15px;color:var(--grey)}
.heading .light{display:block;font-weight:300;color:#888}
.heading .bold{display:block;font-weight:700;color:#6a6a6a}
.tiny{font-size:4.5px;line-height:1.55;color:#777}
.small{font-size:5px;line-height:1.5;color:#555}
.footer{position:absolute;bottom:6px;right:20px;font-size:3.5px;color:#bbb;word-spacing:10px}
.photo{position:absolute}
.tick{color:var(--green);font-weight:700}
.brand{font-family:"Lato",sans-serif;font-weight:700;font-size:6px;color:var(--blue);display:flex;align-items:center;gap:3px;letter-spacing:.3px}
.brand i{display:block;width:7px;height:7px;border-radius:50%;background:var(--green)}
.num-list div{position:absolute;display:flex;align-items:center;gap:10px}
.num-list b{font-family:"Roboto Slab",serif;font-weight:300;font-size:14px;color:var(--blue);width:20px}
</style>
</head>
<body>

<!-- 1 Cover -->
<section class="slide" style="left:20px;top:18px">
  <div class="photo" role="img" aria-label="Smiling young professional woman in an office with colleagues behind her" style="inset:0;background:linear-gradient(110deg,#5d6a72 0%,#b8c1c4 35%,#dfe4e2 60%,#c8ccc4 100%)"></div>
  <div class="abs" style="inset:0;background:#b5d970;clip-path:polygon(185px 0,380px 0,380px 214px,100px 214px)"></div>
  <div class="abs" style="inset:0;background:var(--green);clip-path:polygon(200px 0,380px 0,380px 214px,112px 214px)"></div>
  <div class="abs" style="left:198px;top:46px;font-family:'Roboto Slab',serif;font-weight:700;font-size:13.5px;line-height:1.25;color:#333">INTERNATIONAL<br>CAREER DEVELOPMENT<br>WORKSHOP</div>
  <div class="abs" style="left:198px;top:108px;font-size:7.5px;color:#fff">Feb 2017</div>
  <div class="abs" style="left:198px;top:119px;font-size:6px;color:#fff">Presented by : John Doe</div>
  <div class="abs" style="left:193px;top:175px;width:110px;height:23px;background:#3a3a36;clip-path:polygon(10px 0,100% 0,100% 100%,0 100%);color:#fff;font-size:5.5px;display:flex;align-items:center;justify-content:center">www.company.com</div>
  <div class="abs" style="left:303px;top:175px;width:77px;height:23px;background:#fff;display:flex;align-items:center;justify-content:center"><span class="brand"><i></i>NORTHBAY INTERNSHIPS</span></div>
</section>

<!-- 2 Contents -->
<section class="slide" style="left:408px;top:18px">
  <div class="corner"><span>2</span></div>
  <h2 class="heading" style="left:48px;top:8px"><span class="light">Content at</span><span class="bold">Glance</span></h2>
  <div class="num-list">
    <div style="left:48px;top:66px"><b>01</b><p class="tiny">Lorem ipsum dolor sit amet, ligula<br>suspendisse nulla pretium</p></div>
    <div style="left:48px;top:88px"><b>02</b><p class="tiny">Lorem ipsum dolor sit amet, ligula<br>suspendisse nulla pretium</p></div>
    <div style="left:48px;top:110px"><b>03</b><p class="tiny">Lorem ipsum dolor sit amet, ligula<br>suspendisse nulla pretium</p></div>
    <div style="left:48px;top:131px"><b>04</b><p class="tiny">Lorem ipsum dolor sit amet, ligula<br>suspendisse nulla pretium</p></div>
    <div style="left:195px;top:66px"><b>05</b><p class="tiny">Lorem ipsum dolor sit amet, ligula<br>suspendisse nulla pretium</p></div>
    <div style="left:195px;top:88px"><b>06</b><p class="tiny">Lorem ipsum dolor sit amet, ligula<br>suspendisse nulla pretium</p></div>
    <div style="left:195px;top:110px"><b>07</b><p class="tiny">Lorem ipsum dolor sit amet, ligula<br>suspendisse nulla pretium</p></div>
  </div>
  <div class="footer">www.company.com · Company · @Company · Company</div>
</section>

<!-- 3 Quote -->
<section class="slide" style="left:796px;top:18px">
  <div class="corner"><span>3</span></div>
  <h2 class="heading" style="left:48px;top:8px"><span class="light">Leadership Training</span><span class="bold">Quote</span></h2>
  <div class="abs" style="left:44px;top:50px;width:297px;height:136px;border:1px solid #ddd;padding:5px">
    <div role="img" aria-label="Confident businessman in a suit gesturing with an open hand" style="width:100%;height:100%;background:linear-gradient(90deg,#f2f4f5 0%,#e7eaec 45%,#9aa3a8 75%,#cfd5d8 100%)"></div>
  </div>
  <div class="abs" style="left:53px;top:68px;background:var(--green);color:#fff;font-size:13.5px;padding:0 13px 0 2px;line-height:16px">International Career</div>
  <div class="abs" style="left:53px;top:88px;background:var(--green);color:#fff;font-size:13.5px;padding:0 12px 0 2px;line-height:16px">Development</div>
  <div class="footer">www.company.com · Company · @Company · Company</div>
</section>

<!-- 4 Strength -->
<section class="slide" style="left:20px;top:239px">
  <div class="corner"><span>4</span></div>
  <h2 class="heading" style="left:22px;top:43px"><span class="light">Match Your</span><span class="bold">Stregth Here</span></h2>
  <div class="abs" style="left:22px;top:86px;width:142px;height:1px;background:var(--green)"></div>
  <div class="abs tiny" style="left:22px;top:100px">
    <div><span class="tick">✓</span> Lorem ipsum dolor sit.</div><div><span class="tick">✓</span> Amet, ligula suspendisse.</div><div><span class="tick">✓</span> Nulla pretium, rhoncus.</div><div><span class="tick">✓</span> Tempor fermentum.</div>
  </div>
  <div class="abs tiny" style="left:87px;top:100px">
    <div><span class="tick">✓</span> Lorem ipsum dolor sit.</div><div><span class="tick">✓</span> Amet, ligula suspendisse.</div><div><span class="tick">✓</span> Nulla pretium, rhoncus.</div><div><span class="tick">✓</span> Tempor fermentum.</div>
  </div>
  <p class="abs tiny" style="left:22px;top:146px;width:150px;color:#333">Lorem ipsum dolor sit amet, consectetur adipiscing elit. Etiam et libero quis risus finibus sollicitudin nec vel nibh. Praesent condimentum arcu sed congue bibendum.</p>
  <div class="photo" role="img" aria-label="Hand writing with a pen on paper" style="left:190px;top:0;width:190px;height:214px;background:linear-gradient(160deg,#f3f3f3 0%,#e3e3e3 55%,#cfcfcf 100%)"></div>
  <p class="abs" style="left:198px;top:80px;width:176px;text-align:center;font-family:'Roboto Slab',serif;font-size:9.5px;line-height:1.5;color:#333">Lorem ipsum dolor sit amet, consectetur adipiscing elit. Etiam et libero quis risus finibus sollicitudin nec vel nibh.</p>
  <div class="footer">www.company.com · Company · @Company · Company</div>
</section>

<!-- 5 Integrity -->
<section class="slide" style="left:408px;top:239px">
  <div class="corner"><span>5</span></div>
  <div class="abs" style="inset:0;background:#eeeeee;clip-path:polygon(0 0,180px 0,136px 214px,0 214px)"></div>
  <h2 class="heading" style="left:40px;top:43px;text-align:center"><span class="light">Place Your</span><span class="bold">Header Here</span></h2>
  <p class="abs tiny" style="left:24px;top:102px;width:128px;text-align:center">Lorem ipsum dolor sit amet, consectetur adipiscing elit. Aenean commodo ligula eget dolor. Aenean massa. Cum sociis natoque penatibus et magnis dis parturient montes, nascetur ridiculus mus.</p>
  <h3 class="heading" style="left:206px;top:33px;font-size:10px"><span class="light">The New Experience of</span><span class="bold">Professional Integrity</span></h3>
  <p class="abs tiny" style="left:206px;top:67px;width:154px;font-size:3.8px;color:#333">Lorem ipsum dolor sit amet, consectetuer adipiscing elit. Aenean commodo ligula eget dolor. Aenean massa. Cum sociis natoque penatibus et magnis dis parturient montes, nascetur ridiculus mus. Donec quam felis, ultricies nec, pellentesque eu, pretium quis, sem.</p>
  <div class="abs tiny" style="left:206px;top:105px;width:150px;font-size:3.8px">
    <div style="display:flex;gap:10px;margin-bottom:12px"><span class="tick" style="font-size:9px">✓</span><span>Lorem ipsum dolor sit amet, consectetur adipiscing elit. Etiam et libero quis risus finibus sollicitudin nec vel nibh.</span></div>
    <div style="display:flex;gap:10px;margin-bottom:12px"><span class="tick" style="font-size:9px">✓</span><span>Lorem ipsum dolor sit amet, consectetur adipiscing elit. Etiam et libero quis risus finibus sollicitudin nec vel nibh.</span></div>
    <div style="display:flex;gap:10px"><span class="tick" style="font-size:9px">✓</span><span>Lorem ipsum dolor sit amet, consectetur adipiscing elit. Etiam et libero quis risus finibus sollicitudin nec vel nibh.</span></div>
  </div>
  <div class="footer">www.company.com · Company · @Company · Company</div>
</section>

<!-- 6 Actionable -->
<section class="slide" style="left:796px;top:239px">
  <div class="corner" style="z-index:2"><span>6</span></div>
  <div class="photo" role="img" aria-label="Businesswoman presenting to seated colleagues in a bright meeting room" style="inset:0;background:linear-gradient(120deg,#f4f5f6 0%,#dfe3e6 50%,#b9bcbf 100%);clip-path:polygon(248px 0,380px 0,380px 214px,150px 214px)"></div>
  <div class="abs" style="inset:0;background:#4d7ec0;clip-path:polygon(244px 0,253px 0,176px 128px,167px 128px)"></div>
  <div class="abs" style="inset:0;background:var(--green);clip-path:polygon(97px 104px,202px 104px,137px 214px,50px 214px)"></div>
  <h2 class="heading" style="left:0;top:14px;width:96px;text-align:right;font-size:10.5px"><span class="light">Actionable</span><span class="bold">Professional</span><span class="bold">Integrity</span></h2>
  <div class="abs" style="left:106px;top:18px;display:flex;align-items:center;gap:8px;font-size:8.5px;color:#777">
    <svg width="14" height="9" viewBox="0 0 14 9"><g fill="#555"><rect x="0" y="0" width="2" height="2"/><rect x="3" y="0" width="11" height="2"/><rect x="0" y="3.5" width="2" height="2"/><rect x="3" y="3.5" width="11" height="2"/><rect x="0" y="7" width="2" height="2"/><rect x="3" y="7" width="11" height="2"/></g></svg>
    Header Here</div>
  <div class="abs" style="left:106px;top:37px;font-size:6.5px;color:var(--green);letter-spacing:.2px">SUB HEADING TEXT</div>
  <p class="abs tiny" style="left:106px;top:47px;width:104px;font-size:3.8px;color:#333">Lorem ipsum dolor sit amet, consectetur adipiscing elit. Etiam et libero quis risus finibus sollicitudin nec vel nibh. Praesent condimentum arcu sed congue bibendum.</p>
  <div class="abs" style="left:96px;top:114px;color:#fff;font-size:3.8px;line-height:1.5">
    <div style="display:flex;gap:4px;align-items:center"><b style="font-family:'Roboto Slab';font-size:11px">01</b><span>Lorem ipsum dolor sit amet, consectetur<br>adipiscing elit. Etiam et libero</span></div>
    <div style="display:flex;gap:4px;align-items:center;margin-left:-12px;margin-top:6px"><b style="font-family:'Roboto Slab';font-size:11px">02</b><span>Lorem ipsum dolor sit amet, consectetur<br>adipiscing elit. Etiam et libero</span></div>
    <div style="display:flex;gap:4px;align-items:center;margin-left:-24px;margin-top:6px"><b style="font-family:'Roboto Slab';font-size:11px">03</b><span>Lorem ipsum dolor sit amet, consectetur<br>adipiscing elit. Etiam et libero</span></div>
    <div style="display:flex;gap:4px;align-items:center;margin-left:-36px;margin-top:6px"><b style="font-family:'Roboto Slab';font-size:11px">04</b><span>Lorem ipsum dolor sit amet, consectetur<br>adipiscing elit. Etiam et libero</span></div>
  </div>
</section>

<!-- 7 Values -->
<section class="slide" style="left:20px;top:461px">
  <div class="corner"><span>7</span></div>
  <h2 class="heading" style="left:48px;top:8px"><span class="light">Developing</span><span class="bold">Your Values</span></h2>
  <p class="abs" style="left:40px;top:50px;width:300px;text-align:center;font-size:9px;line-height:1.4;color:#777">“ <b style="color:var(--blue)">Lorem ipsum</b> dolor sit amet, consectetuer adipiscing elit.<br>Aenean commodo ligula eget dolor. ”</p>
  <div class="abs" style="left:60px;top:85px;width:262px;height:1px;background:#aaa"></div>
  <div class="abs tiny" style="left:62px;top:93px;width:230px;font-size:3.8px">
    <div style="display:flex;gap:12px;margin-bottom:10px"><span class="tick" style="font-size:9px">✓</span><span>Lorem ipsum dolor sit amet, consectetur adipiscing elit. Etiam et libero quis risus finibus sollicitudin nec vel nibh. Praesent condimentum arcu sed congue bibendum.</span></div>
    <div style="display:flex;gap:12px;margin-bottom:10px"><span class="tick" style="font-size:9px">✓</span><span>Lorem ipsum dolor sit amet, consectetur adipiscing elit. Etiam et libero quis risus finibus sollicitudin nec vel nibh. Praesent condimentum arcu sed congue bibendum.</span></div>
    <div style="display:flex;gap:12px"><span class="tick" style="font-size:9px">✓</span><span>Lorem ipsum dolor sit amet, consectetur adipiscing elit. Etiam et libero quis risus finibus sollicitudin nec vel nibh. Praesent condimentum arcu sed congue bibendum.</span></div>
  </div>
  <p class="abs tiny" style="left:45px;top:170px;width:290px;text-align:center;font-size:3.8px">Lorem ipsum dolor sit amet, ligula suspendisse nulla pretium, rhoncus tempor fermentum, enim integer ad vestibulum volutpat. Nisl rhoncus turpis est, vel elit, congue wisi enim nunc ultricies sit, magna tincidunt. Maecenas aliquam maecenas ligula nostra, accumsan taciti.</p>
  <div class="footer">www.company.com · Company · @Company · Company</div>
</section>

<!-- 8 Implementation -->
<section class="slide" style="left:408px;top:461px">
  <div class="corner"><span>8</span></div>
  <div class="abs" style="left:0;top:0;width:120px;height:214px;background:var(--green)"></div>
  <h2 class="heading" style="left:13px;top:37px;font-size:11px;color:#fff"><span class="light" style="color:#fff">Place Your</span><span class="bold" style="color:#fff">Header</span><span class="bold" style="color:#fff">Here</span></h2>
  <p class="abs tiny" style="left:13px;top:95px;width:100px;color:#fff;font-size:3.8px;text-align:justify">Lorem ipsum dolor sit amet, consectetur adipiscing elit. Etiam et libero quis risus finibus sollicitudin nec vel nibh. Praesent condimentum arcu sed congue bibendum.</p>
  <div class="abs" style="left:13px;top:150px;width:87px;height:13px;background:#fff;color:#444;font-size:5.5px;display:flex;align-items:center;justify-content:center">VISIT US</div>
  <div class="photo" role="img" aria-label="Young woman in a shirt and blazer reading documents at a desk" style="left:120px;top:0;width:98px;height:214px;background:linear-gradient(180deg,#d9d3ca 0%,#a99c8c 40%,#3c4a66 75%,#e4e0d8 100%)"></div>
  <div class="abs" style="left:258px;top:23px">
    <div style="display:flex;gap:12px;align-items:center;height:38px"><svg width="16" height="16"><circle cx="8" cy="8" r="7.5" fill="none" stroke="#9bcb3b" stroke-width=".8"/><circle cx="8" cy="8" r="3" fill="none" stroke="#9bcb3b" stroke-width="1.2"/></svg><p class="tiny" style="font-size:3.8px"><b style="color:#9bcb3b">Implementation</b><br>suspendisse nulla pretium</p></div>
    <div style="display:flex;gap:12px;align-items:center;height:38px"><svg width="16" height="16"><circle cx="8" cy="8" r="7.5" fill="none" stroke="#f39c1e" stroke-width=".8"/><rect x="5" y="6" width="6" height="4" fill="#f39c1e"/></svg><p class="tiny" style="font-size:3.8px"><b style="color:#f39c1e">Implementation</b><br>suspendisse nulla pretium</p></div>
    <div style="display:flex;gap:12px;align-items:center;height:38px"><svg width="16" height="16"><circle cx="8" cy="8" r="7.5" fill="none" stroke="#1fa89a" stroke-width=".8"/><circle cx="8" cy="6.5" r="1.8" fill="#1fa89a"/><rect x="5" y="9" width="6" height="2.5" rx="1" fill="#1fa89a"/></svg><p class="tiny" style="font-size:3.8px"><b style="color:#1fa89a">Implementation</b><br>suspendisse nulla pretium</p></div>
    <div style="display:flex;gap:12px;align-items:center;height:38px"><svg width="16" height="16"><circle cx="8" cy="8" r="7.5" fill="none" stroke="#2b7cc8" stroke-width=".8"/><path d="M8 12 L5.5 7.5 A2.7 2.7 0 1 1 10.5 7.5 Z" fill="#2b7cc8"/></svg><p class="tiny" style="font-size:3.8px"><b style="color:#2b7cc8">Implementation</b><br>suspendisse nulla pretium</p></div>
    <div style="display:flex;gap:12px;align-items:center;height:38px"><svg width="16" height="16"><circle cx="8" cy="8" r="7.5" fill="none" stroke="#9b6bd6" stroke-width=".8"/><rect x="5" y="5.5" width="6" height="1" fill="#9b6bd6"/><rect x="5" y="7.5" width="6" height="1" fill="#9b6bd6"/><rect x="5" y="9.5" width="6" height="1" fill="#9b6bd6"/></svg><p class="tiny" style="font-size:3.8px"><b style="color:#9b6bd6">Implementation</b><br>suspendisse nulla pretium</p></div>
  </div>
  <div class="footer">www.company.com · Company · @Company · Company</div>
</section>

<!-- 9 Key steps -->
<section class="slide" style="left:796px;top:461px">
  <div class="corner"><span>9</span></div>
  <h2 class="heading" style="left:48px;top:8px"><span class="light">4 Key Successful</span><span class="bold">Your Resume</span></h2>
  <div class="abs" style="left:0;top:57px;width:380px;height:85px;background:var(--dark-band)"></div>
  <svg class="abs" style="left:0;top:57px" width="380" height="85" viewBox="0 0 380 85">
    <line x1="18" y1="33" x2="370" y2="33" stroke="#bbb" stroke-width=".6" stroke-dasharray="1.5 1.5"/>
    <circle cx="18" cy="33" r="2" fill="#ddd"/><circle cx="370" cy="33" r="2" fill="#ddd"/>
    <g fill="var(--dark-band)" stroke="#fff" stroke-width=".9">
      <circle cx="51" cy="33" r="17"/><circle cx="145" cy="33" r="17"/><circle cx="240" cy="33" r="17"/><circle cx="334" cy="33" r="17"/>
    </g>
    <g fill="#fff">
      <circle cx="49" cy="29" r="3"/><rect x="44" y="33" width="10" height="6" rx="2"/>
      <rect x="139" y="28" width="12" height="3"/><rect x="141" y="32" width="8" height="7"/>
      <rect x="238" y="25" width="1.2" height="15"/><path d="M239 26 L246 29 L239 32 Z"/>
      <circle cx="336" cy="29" r="3.5"/><rect x="327" y="35" width="12" height="3" rx="1"/>
    </g>
    <g fill="#fff" font-family="Lato,sans-serif" font-size="4.5" text-anchor="middle">
      <text x="51" y="66">HEADING</text><text x="51" y="71">HERE</text>
      <text x="145" y="66">HEADING</text><text x="145" y="71">HERE</text>
      <text x="240" y="66">HEADING</text><text x="240" y="71">HERE</text>
      <text x="334" y="66">HEADING</text><text x="334" y="71">HERE</text>
    </g>
  </svg>
  <p class="abs tiny" style="left:25px;top:164px;width:330px;text-align:center;font-size:3.8px">Lorem ipsum dolor sit amet, ligula suspendisse nulla pretium, rhoncus tempor fermentum, enim integer ad vestibulum volutpat. Nisl rhoncus turpis est, vel elit, congue wisi enim nunc ultricies sit, magna tincidunt. Maecenas aliquam maecenas ligula nostra, accumsan taciti. Sociis mauris in integer, a dolor netus non dui aliquet, sagittis felis sodales, dolor sociis mauris, vel eu libero cras.</p>
  <div class="footer">www.company.com · Company · @Company · Company</div>
</section>

<!-- 10 Inspiration -->
<section class="slide" style="left:20px;top:682px">
  <div class="corner"><span>10</span></div>
  <h2 class="abs" style="left:0;top:32px;width:380px;text-align:center;font-family:'Roboto Slab',serif;font-size:14px;color:#888;font-weight:300">PROFESSIONAL <b style="font-weight:700;color:#6a6a6a">INSPIRATION</b></h2>
  <div class="abs" style="left:0;top:56px;width:380px;text-align:center;font-size:6px;color:var(--green)">HEADING HERE</div>
  <p class="abs tiny" style="left:50px;top:71px;width:280px;text-align:center;font-size:3.8px">Lorem ipsum dolor sit amet, ligula suspendisse nulla pretium, rhoncus tempor fermentum, enim integer ad vestibulum volutpat. Nisl rhoncus turpis est, vel elit, congue wisi enim nunc ultricies sit, magna tincidunt. Maecenas aliquam maecenas ligula nostra, accumsan taciti.</p>
  <div class="abs" style="left:0;top:107px;width:380px;height:107px;display:grid;grid-template-columns:repeat(7,1fr);grid-template-rows:1fr 1fr">
    <div role="img" aria-label="Portrait of a smiling businessman" style="background:linear-gradient(160deg,#d6dadd,#7b8389)"></div>
    <div role="img" aria-label="Portrait of a woman on the phone" style="background:linear-gradient(160deg,#d9d4cf,#8c8a88)"></div>
    <div style="background:var(--green);color:#fff;font-size:3.8px;padding:9px 8px;line-height:1.5"><b>HEADING HERE</b><br>suspendisse nulla pretium</div>
    <div role="img" aria-label="Portrait of a smiling businessman" style="background:linear-gradient(160deg,#d6dadd,#7b8389)"></div>
    <div role="img" aria-label="Portrait of a smiling businessman" style="background:linear-gradient(160deg,#dfe2e4,#858c92)"></div>
    <div role="img" aria-label="Portrait of a woman on the phone" style="background:linear-gradient(160deg,#d9d4cf,#8c8a88)"></div>
    <div style="background:var(--blue);color:#fff;font-size:3.8px;padding:9px 8px;line-height:1.5"><b>HEADING HERE</b><br>suspendisse nulla pretium</div>
    <div role="img" aria-label="Portrait of a smiling businessman" style="background:linear-gradient(160deg,#dfe2e4,#7b8389)"></div>
    <div style="background:var(--blue);color:#fff;font-size:3.8px;padding:9px 8px;line-height:1.5"><b>HEADING HERE</b><br>suspendisse nulla pretium</div>
    <div role="img" aria-label="Portrait of a smiling businessman" style="background:linear-gradient(160deg,#d6dadd,#7b8389)"></div>
    <div role="img" aria-label="Portrait of a woman on the phone" style="background:linear-gradient(160deg,#d9d4cf,#8c8a88)"></div>
    <div style="background:var(--green);color:#fff;font-size:3.8px;padding:9px 8px;line-height:1.5"><b>HEADING HERE</b><br>suspendisse nulla pretium</div>
    <div role="img" aria-label="Portrait of a smiling businessman" style="background:linear-gradient(160deg,#dfe2e4,#858c92)"></div>
    <div role="img" aria-label="Portrait of a smiling businessman" style="background:linear-gradient(160deg,#d6dadd,#7b8389)"></div>
  </div>
</section>

<!-- 11 Timeline -->
<section class="slide" style="left:408px;top:682px">
  <div class="corner"><span>11</span></div>
  <h2 class="heading" style="left:48px;top:8px"><span class="light">The Job Search</span><span class="bold">Evolution</span></h2>
  <svg class="abs" style="left:0;top:0" width="380" height="214" viewBox="0 0 380 214">
    <rect x="28" y="119" width="314" height="3" fill="var(--green)"/>
    <g stroke="#999" stroke-width=".5" stroke-dasharray="1.5 1.5">
      <line x1="92" y1="82" x2="92" y2="110"/><line x1="171" y1="82" x2="171" y2="110"/><line x1="249" y1="82" x2="249" y2="110"/>
      <line x1="133" y1="130" x2="133" y2="160"/><line x1="211" y1="130" x2="211" y2="160"/><line x1="289" y1="130" x2="289" y2="160"/>
    </g>
    <circle cx="131" cy="106" r="4" fill="#6aa82f"/>
    <rect x="209" y="101" width="7" height="9" rx="1" fill="none" stroke="#2b7cc8" stroke-width="1.2"/>
    <circle cx="288" cy="105" r="3" fill="#f39c1e"/><rect x="286.5" y="100" width="2" height="4" fill="#f39c1e"/>
    <rect x="88" y="132" width="10" height="7" fill="none" stroke="#2b7cc8" stroke-width="1"/>
    <circle cx="164" cy="135" r="2" fill="#f39c1e"/><circle cx="170" cy="133" r="2" fill="#f39c1e"/><circle cx="176" cy="135" r="2" fill="#f39c1e"/>
    <circle cx="249" cy="136" r="4" fill="#3a8c3a"/>
  </svg>
  <div class="abs tiny" style="left:68px;top:58px;width:58px;font-size:3.5px;line-height:1.4"><b style="color:#333">White Collar Jobs</b><br>Lorem ipsum dolor sit amet consectetur adipiscing elit sed do eiusmod tempor</div>
  <div class="abs tiny" style="left:147px;top:58px;width:58px;font-size:3.5px;line-height:1.4"><b style="color:#333">Mobile Phone</b><br>Lorem ipsum dolor sit amet consectetur adipiscing elit sed do eiusmod tempor</div>
  <div class="abs tiny" style="left:225px;top:58px;width:58px;font-size:3.5px;line-height:1.4"><b style="color:#333">Marketplace Jobs</b><br>Lorem ipsum dolor sit amet consectetur adipiscing elit sed do eiusmod tempor</div>
  <div class="abs tiny" style="left:107px;top:164px;width:58px;font-size:3.5px;line-height:1.4"><b style="color:#333">Newspaper Ads</b><br>Lorem ipsum dolor sit amet consectetur adipiscing elit sed do eiusmod tempor</div>
  <div class="abs tiny" style="left:185px;top:164px;width:58px;font-size:3.5px;line-height:1.4"><b style="color:#333">Online Search</b><br>Lorem ipsum dolor sit amet consectetur adipiscing elit sed do eiusmod tempor</div>
  <div class="abs tiny" style="left:263px;top:164px;width:58px;font-size:3.5px;line-height:1.4"><b style="color:#333">Social Media</b><br>Lorem ipsum dolor sit amet consectetur adipiscing elit sed do eiusmod tempor</div>
  <div class="footer">www.company.com · Company · @Company · Company</div>
</section>

<!-- 12 Interview -->
<section class="slide" style="left:796px;top:682px">
  <div class="corner"><span>12</span></div>
  <div class="photo" role="img" aria-label="Person reviewing printed papers at a desk with a laptop" style="left:0;top:0;width:163px;height:214px;background:linear-gradient(140deg,#6b5445 0%,#b49a86 40%,#e6e1dc 70%,#cfcac4 100%)"></div>
  <h2 class="heading" style="left:172px;top:8px"><span class="light">Interview</span><span class="bold">Information</span></h2>
  <p class="abs tiny" style="left:170px;top:60px;width:192px;font-size:3.8px">Lorem ipsum dolor sit amet, ligula suspendisse nulla pretium, rhoncus tempor fermentum, enim integer ad vestibulum volutpat. Nisl rhoncus turpis est, vel elit, congue wisi enim nunc ultricies sit, magna tincidunt. Maecenas aliquam maecenas ligula nostra, accumsan taciti.</p>
  <div class="abs" style="left:170px;top:103px;display:grid;grid-template-columns:100px 100px;row-gap:9px">
    <div style="display:flex;gap:6px;align-items:center"><b style="background:var(--blue);color:#fff;font-size:7px;font-weight:400;width:13px;height:13px;display:flex;align-items:center;justify-content:center">01</b><span class="tiny" style="font-size:3.6px">Lorem ipsum dolor sit amet, ligula<br>suspendisse nulla pretium</span></div>
    <div style="display:flex;gap:6px;align-items:center"><b style="background:var(--blue);color:#fff;font-size:7px;font-weight:400;width:13px;height:13px;display:flex;align-items:center;justify-content:center">04</b><span class="tiny" style="font-size:3.6px">Lorem ipsum dolor sit amet, ligula<br>suspendisse nulla pretium</span></div>
    <div style="display:flex;gap:6px;align-items:center"><b style="background:var(--green);color:#fff;font-size:7px;font-weight:400;width:13px;height:13px;display:flex;align-items:center;justify-content:center">02</b><span class="tiny" style="font-size:3.6px">Lorem ipsum dolor sit amet, ligula<br>suspendisse nulla pretium</span></div>
    <div style="display:flex;gap:6px;align-items:center"><b style="background:var(--green);color:#fff;font-size:7px;font-weight:400;width:13px;height:13px;display:flex;align-items:center;justify-content:center">05</b><span class="tiny" style="font-size:3.6px">Lorem ipsum dolor sit amet, ligula<br>suspendisse nulla pretium</span></div>
    <div style="display:flex;gap:6px;align-items:center"><b style="background:#c4c4c4;color:#fff;font-size:7px;font-weight:400;width:13px;height:13px;display:flex;align-items:center;justify-content:center">03</b><span class="tiny" style="font-size:3.6px">Lorem ipsum dolor sit amet, ligula<br>suspendisse nulla pretium</span></div>
    <div style="display:flex;gap:6px;align-items:center"><b style="background:#c4c4c4;color:#fff;font-size:7px;font-weight:400;width:13px;height:13px;display:flex;align-items:center;justify-content:center">06</b><span class="tiny" style="font-size:3.6px">Lorem ipsum dolor sit amet, ligula<br>suspendisse nulla pretium</span></div>
  </div>
  <div class="footer">www.company.com · Company · @Company · Company</div>
</section>

<!-- 13 Do / Don't -->
<section class="slide" style="left:20px;top:904px">
  <div class="corner"><span>13</span></div>
  <h2 class="heading" style="left:20px;top:34px;width:160px;text-align:right"><span class="light">You Should</span><span class="bold">Do This</span></h2>
  <div class="abs" style="left:20px;top:72px;width:160px;height:1px;background:var(--green)"></div>
  <div class="abs tiny" style="left:20px;top:85px;width:160px;text-align:right;font-size:4px">
    <div>Lorem ipsum dolor sit. <span style="color:#2b7cc8">✓</span></div><div style="margin-top:3px">Amet, ligula suspendisse. <span style="color:#2b7cc8">✓</span></div><div style="margin-top:3px">Nulla pretium, rhoncus. <span style="color:#2b7cc8">✓</span></div><div style="margin-top:3px">Tempor fermentum. <span style="color:#2b7cc8">✓</span></div>
  </div>
  <p class="abs tiny" style="left:30px;top:138px;width:150px;text-align:right;font-size:3.8px;color:#333">Lorem ipsum dolor sit amet, consectetur adipiscing elit. Etiam et libero quis risus finibus sollicitudin nec vel nibh. Praesent condimentum arcu sed congue bibendum.</p>
  <h2 class="heading" style="left:221px;top:34px"><span class="light">You Should</span><span class="bold">Don’t Do This</span></h2>
  <div class="abs" style="left:221px;top:72px;width:142px;height:1px;background:#f0743b"></div>
  <div class="abs tiny" style="left:221px;top:85px;font-size:4px">
    <div><span style="color:#f0743b">✕</span> Lorem ipsum dolor sit.</div><div style="margin-top:3px"><span style="color:#f0743b">✕</span> Amet, ligula suspendisse.</div><div style="margin-top:3px"><span style="color:#f0743b">✕</span> Nulla pretium, rhoncus.</div><div style="margin-top:3px"><span style="color:#f0743b">✕</span> Tempor fermentum.</div>
  </div>
  <p class="abs tiny" style="left:221px;top:138px;width:150px;font-size:3.8px;color:#333">Lorem ipsum dolor sit amet, consectetur adipiscing elit. Etiam et libero quis risus finibus sollicitudin nec vel nibh. Praesent condimentum arcu sed congue bibendum.</p>
  <div class="footer">www.company.com · Company · @Company · Company</div>
</section>

<!-- 14 Location -->
<section class="slide" style="left:408px;top:904px">
  <div class="corner"><span>14</span></div>
  <h2 class="heading" style="left:48px;top:8px"><span class="light">The Event</span><span class="bold">Location</span></h2>
  <div class="abs" style="left:23px;top:49px;width:334px;height:135px;border:1px solid #e2e2e2;padding:3px">
    <div role="img" aria-label="Road map of the region around the event venue" style="width:100%;height:90px;background:linear-gradient(135deg,#ece6d8 0%,#e2dccb 50%,#d9e2cf 100%)"></div>
    <div style="height:39px;background:var(--green);display:flex;align-items:center;justify-content:space-around;padding:0 10px;color:#fff;font-size:5px;line-height:1.4">
      <div style="display:flex;gap:8px;align-items:center"><svg width="20" height="20"><circle cx="10" cy="10" r="9.5" fill="none" stroke="#fff" stroke-width=".8"/><path d="M7 6 L9 6 L10 9 L8.5 10 Q10 12.5 11.5 12.5 L12.5 11 L15 12 L15 14 Q9 15 6 8 Z" fill="none" stroke="#fff" stroke-width=".8"/></svg><span>CALL US<br>+1 555 014 2280</span></div>
      <div style="display:flex;gap:8px;align-items:center"><svg width="20" height="20"><circle cx="10" cy="10" r="9.5" fill="none" stroke="#fff" stroke-width=".8"/><rect x="5" y="6.5" width="10" height="7" fill="none" stroke="#fff" stroke-width=".8"/><path d="M5 6.5 L10 10.5 L15 6.5" fill="none" stroke="#fff" stroke-width=".8"/></svg><span>EMAIL<br>info@northbayevents.org</span></div>
      <div style="display:flex;gap:8px;align-items:center"><svg width="20" height="20"><circle cx="10" cy="10" r="9.5" fill="none" stroke="#fff" stroke-width=".8"/><path d="M5.5 10 L10 5.5 L14.5 10 M7 9 L7 14.5 L13 14.5 L13 9" fill="none" stroke="#fff" stroke-width=".8"/></svg><span>VISIT US<br>Harbor Lane 42</span></div>
    </div>
  </div>
  <div class="abs" style="left:197px;top:86px;background:var(--green);color:#fff;font-size:4.5px;padding:2px 5px">WE ARE HERE</div>
  <div class="footer">www.company.com · Company · @Company · Company</div>
</section>

<!-- 15 Q&A -->
<section class="slide" style="left:796px;top:904px">
  <div class="photo" role="img" aria-label="Hands typing on a laptop keyboard beside a notebook" style="inset:0;background:linear-gradient(120deg,#3d3f42 0%,#7d7a77 35%,#b9b4ae 60%,#d3cec8 100%)"></div>
  <div class="abs" style="inset:0;background:rgba(155,203,59,.92);clip-path:polygon(205px 0,380px 0,380px 214px,85px 214px)"></div>
  <div class="abs" style="left:268px;top:48px;width:36px;height:36px;border:1.5px solid #fff;border-radius:50%;color:#fff;font-family:'Roboto Slab',serif;font-size:20px;display:flex;align-items:center;justify-content:center">?</div>
  <div class="abs" style="left:190px;top:94px;width:190px;text-align:center;color:#fff;font-family:'Roboto Slab',serif;font-weight:700;font-size:12.5px;letter-spacing:.3px">Question Answer</div>
  <p class="abs" style="left:212px;top:112px;width:148px;text-align:center;color:#fff;font-size:4.5px;line-height:1.4">Pack my box with five dozen liquor jugs. How vexingly quick daft zebras jump over the wall.</p>
  <div class="abs" style="left:193px;top:175px;width:110px;height:23px;background:#3a3a36;clip-path:polygon(10px 0,100% 0,100% 100%,0 100%);color:#fff;font-size:5.5px;display:flex;align-items:center;justify-content:center">www.company.com</div>
  <div class="abs" style="left:303px;top:175px;width:77px;height:23px;background:#fff;display:flex;align-items:center;justify-content:center"><span class="brand"><i></i>NORTHBAY INTERNSHIPS</span></div>
</section>

</body>
</html>
```